Brochure Cover and Back pages

We are a US-based cosmetics company that sells state-of-the-art skin care products, including advanced anti-aging serums, natural mineral sunscreens, organic antioxidant moisturizers, and organic face cleansers. We need a product brochure. We already have chosen a design for the layout of the product info pages. But we still need a cover page and a back page. We are looking for simple but elegant design for the cover page. The back page is less important and we already know what we want on the back page. It will be the company's mission statement and at the bottom, the company URL, phone number, etc.

The brochure has two folds. So there will be three panels on both sides. The size of each panel is 16.5 (l) x 9.5 (w) cm.

At the end of the project, we expect the designer to integrate all the pages so that the finished copy is read to be sent off to a printing service for printing.

All the product info pages are attached. Also attached are the text (info) to go on the back page, company logo with and without the tagline, the icon in the logo.

YOu are welcome to visit our website www.morvask.com to learn about our products.

Industry/Entity Type

Cosmetics

```html
<!DOCTYPE html>
<html lang="en">
<head>
<meta charset="utf-8">
<title>Morvask Brochure</title>
<link href="https://fonts.googleapis.com/css2?family=PT+Sans:wght@400;700&family=PT+Sans+Narrow:wght@700&display=swap" rel="stylesheet">
<style>
  :root {
    --stage: #000000;
    --paper: #ffffff;
    --cover-grey: #e4e5ea;
    --row-grey: #ebebef;
    --ink: #1a1a1a;
    --body-ink: #2b2b2b;
    --muted: #9a9a9f;
    --magenta: #e5097f;
    --orange: #f7941d;
    --rule: #d8d8dc;
  }
  * { box-sizing: border-box; margin: 0; padding: 0; }
  html, body { width: 811px; height: 1200px; overflow: hidden; background: var(--stage); }
  body { position: relative; font-family: "PT Sans", Arial, sans-serif; color: var(--ink); }

  .page { position: absolute; overflow: hidden; }
  .back-page { left: 75px; top: 15px; width: 332px; height: 580px;
    background: linear-gradient(90deg, #e9eaee 0%, #e2e3e8 90%, #cfd0d6 100%); }
  .cover-page { left: 407px; top: 15px; width: 333px; height: 580px;
    background: linear-gradient(90deg, #e8e8ea 0%, #ffffff 6%, #ffffff 100%); }

  .brand-name { font-family: "PT Sans", Arial, sans-serif; font-weight: 400; color: var(--ink);
    letter-spacing: 1px; text-align: center; position: absolute; left: 0; width: 100%; }
  .back-page .brand-name { top: 205px; font-size: 32px; }
  .cover-page .brand-name { top: 34px; font-size: 36px; }

  .contact { position: absolute; top: 273px; left: 0; width: 100%; text-align: center;
    font-size: 10.5px; line-height: 12px; color: var(--body-ink); }
  .contact .company { font-size: 12px; font-weight: 700; color: var(--ink); margin-bottom: 1px; }
  .contact p + p.gap { margin-top: 11px; }

  .cover-photo { position: absolute; left: 10px; top: 115px; width: 323px; height: 465px;
    background: radial-gradient(ellipse 45% 55% at 50% 45%, #dcb7a0 0%, #c9a189 45%, #f4efec 80%, #ffffff 100%); }

  .inside-page { top: 608px; width: 331px; height: 579px; background: var(--paper); }
  .inside-left { left: 75px; }
  .inside-right { left: 409px; }

  .section-tab { position: absolute; left: 32px; top: 0; width: 270px; height: 48px;
    border-radius: 0 0 7px 7px; color: #fff; font-weight: 700; font-size: 15.5px;
    display: flex; align-items: center; justify-content: center; letter-spacing: 0.2px; }
  .inside-left .section-tab { background: var(--magenta); }
  .inside-right .section-tab { background: var(--orange); }

  .product-row { position: absolute; left: 0; width: 331px; padding: 9px 0 0 30px; }
  .product-row.shaded { background: var(--row-grey); }
  .row-1 { top: 62px; height: 115px; }
  .row-2 { top: 177px; height: 123px; }
  .row-3 { top: 300px; height: 127px; }
  .row-4 { top: 427px; height: 123px; }

  .product-title { font-family: "PT Sans Narrow", "PT Sans", sans-serif; font-weight: 700;
    font-size: 11.5px; letter-spacing: 0.1px; margin-bottom: 9px; }
  .product-text { width: 227px; font-size: 10.5px; line-height: 13px; text-align: justify; color: var(--body-ink); }
  .product-link { font-size: 10.5px; line-height: 13px; display: block; }
  .inside-left .product-link { color: var(--magenta); }
  .inside-right .product-link { color: var(--orange); }

  .product-shot { position: absolute; right: 26px; width: 30px; border-radius: 4px;
    background: linear-gradient(90deg, #e4e4e6 0%, #ffffff 45%, #dcdcde 100%);
    box-shadow: 0 0 0 1px #e2e2e4; }
  .row-1 .product-shot { top: 10px; height: 92px; }
  .row-2 .product-shot { top: 10px; height: 98px; }
  .row-3 .product-shot { top: 18px; height: 100px; }
  .row-4 .product-shot { top: 10px; height: 100px; }
  .inside-right .row-4 .product-shot { top: 14px; height: 96px; }

  .page-footer { position: absolute; left: 0; bottom: 0; width: 100%; height: 29px;
    border-top: 1px solid var(--rule); text-align: center; font-size: 10px; line-height: 28px; color: var(--muted); }
</style>
</head>
<body>

  <section class="page back-page">
    <div class="brand-name">Morvask</div>
    <div class="contact">
      <p class="company">Morvask</p>
      <p>Creating Beauty Solutions through Science</p>
      <p>www.morvask.com</p>
      <p class="gap">Customer Service 1-855-5-Morvsk (855-556-6787)</p>
      <p class="gap">2190 Larkmoor Ave.&nbsp; Suite 400</p>
      <p>Bayfield Hill, CA 94610</p>
    </div>
  </section>

  <section class="page cover-page">
    <div class="brand-name">Morvask</div>
    <div class="cover-photo" role="img" aria-label="Beauty portrait photograph showing renewed skin, cover image"></div>
  </section>

  <section class="page inside-page inside-left">
    <div class="section-tab">LOREM IPSUM DOLOR SIT AMET</div>

    <article class="product-row row-1">
      <h3 class="product-title">LOREM IPSUM DOLOR SIT AMET</h3>
      <p class="product-text">Has enim choro moderatius eu, qui ut labitur sanctus nusquam. Vis in idque animal deseruisse, ad nullam suavitate his, quo ne suavitate disputando. In alia dicat possit pro. Etiam iriure sed ne, per ad natum tollit.</p>
      <a class="product-link">Ad mei probo</a>
      <div class="product-shot" role="img" aria-label="Product bottle photograph"></div>
    </article>

    <article class="product-row row-2 shaded">
      <h3 class="product-title">MEA MALUISSET IRACUNDIA EA.</h3>
      <p class="product-text">Vel erant nostrum an, eu pri novum cotidieque efficiantur, an mazim apeirian per. Per an omnes debitis sensibus, te volumus recteque qualisque mea. Reprimique vituperatoribus sit ut, et posse nonumy bonorum eos.</p>
      <a class="product-link">Ad mei probo</a>
      <div class="product-shot" role="img" aria-label="Serum pump bottle photograph"></div>
    </article>

    <article class="product-row row-3">
      <h3 class="product-title">NO DUO VIDIT SANCTUS</h3>
      <p class="product-text">An pri idque dolorem tacimates. Tation nostrum at sea. Eu alia pertinacia vix, sale molestiae torquatos eum no. Homero voluptua prodesset mea te, ius mazim constituto ad, dignissim gubergren nam an. Vel erant nostrum an, eu pri novum cotidieque efficiantur.</p>
      <a class="product-link">Ad mei probo</a>
      <div class="product-shot" role="img" aria-label="Serum pump bottle photograph"></div>
    </article>

    <article class="product-row row-4 shaded">
      <h3 class="product-title">IUS IN ELABORARET QUAERENDUM</h3>
      <p class="product-text">Pri id mazim fastidii vivendum. Vulputate democritum eam ei, sit probatus necessitatibus at. Ne tota movet efficiantur duo, qui cu mazim munere altera. Vix eu esse laoreet, in case recusabo tractatos eos.</p>
      <a class="product-link">Ad mei probo</a>
      <div class="product-shot" role="img" aria-label="Serum pump bottle photograph"></div>
    </article>

    <footer class="page-footer">lorem ipsum dolor sit amet</footer>
  </section>

  <section class="page inside-page inside-right">
    <div class="section-tab">LOREM IPSUM DOLOR SIT AMET</div>

    <article class="product-row row-1">
      <h3 class="product-title">LOREM IPSUM DOLOR SIT AMET</h3>
      <p class="product-text">Has enim choro moderatius eu, qui ut labitur sanctus nusquam. Vis in idque animal deseruisse, ad nullam suavitate his, quo ne suavitate disputando. In alia dicat possit pro. Etiam iriure sed ne, per ad natum tollit.</p>
      <a class="product-link">Ad mei probo</a>
      <div class="product-shot" role="img" aria-label="Cream tube photograph"></div>
    </article>

    <article class="product-row row-2 shaded">
      <h3 class="product-title">MEA MALUISSET IRACUNDIA EA.</h3>
      <p class="product-text">Vel erant nostrum an, eu pri novum cotidieque efficiantur, an mazim apeirian per. Per an omnes debitis sensibus, te volumus recteque qualisque mea. Reprimique vituperatoribus sit ut, et posse nonumy bonorum eos.</p>
      <a class="product-link">Ad mei probo</a>
      <div class="product-shot" role="img" aria-label="Sunscreen tube photograph"></div>
    </article>

    <article class="product-row row-3">
      <h3 class="product-title">NO DUO VIDIT SANCTUS</h3>
      <p class="product-text">An pri idque dolorem tacimates. Tation nostrum at sea. Eu alia pertinacia vix, sale molestiae torquatos eum no. Homero voluptua prodesset mea te, ius mazim constituto ad, dignissim gubergren nam an. Vel erant nostrum an, eu pri novum cotidieque efficiantur.</p>
      <a class="product-link">Ad mei probo</a>
      <div class="product-shot" role="img" aria-label="Moisturizer bottle photograph"></div>
    </article>

    <article class="product-row row-4 shaded">
      <h3 class="product-title">IUS IN ELABORARET QUAERENDUM</h3>
      <p class="product-text">Pri id mazim fastidii vivendum. Vulputate democritum eam ei, sit probatus necessitatibus at. Ne tota movet efficiantur duo, qui cu mazim munere altera. Vix eu esse laoreet, in case recusabo tractatos eos.</p>
      <a class="product-link">Ad mei probo</a>
      <div class="product-shot" role="img" aria-label="Cleanser bottle photograph"></div>
    </article>

    <footer class="page-footer">lorem ipsum dolor sit amet</footer>
  </section>

</body>
</html>
```